Home inspection business! professional look attracting customers just by looks. Read must haves

its a new business I started on my own for home inspections I would like something very professional to give to real estate agents and clients, its going to have my license number on it my business phone number my name my website as well etc on the back side it will be servicing areas and also what kind of services I offer I also have a business card from someone else the way I would like mine to be. I will attach my logo

Home Inspection

listed in nice to haves

• phone number - 555 293 8471
• website- hollowpinecheck.com
• license number #2938475610
• my name Gavin keropulis
• picture of my logo and me on the front
• on the back of the card. stating I am servicing All of New York and Long Island
• also services I will offer will be home inspection -mold inspection -lead inspection -radon inspection -Termite Inspection -Infared Scan.
• and also we provide inspections for single family homes condos co-ops town-homes
• and commercial property
• same colors as the logos and also if you recommend fonts to look like the logo not sure up to you

```html
<!DOCTYPE html>
<html lang="en">
<head>
<meta charset="utf-8">
<title>Hollow Pine Home Inspectors – Business Card</title>
<link rel="stylesheet" href="https://fonts.googleapis.com/css2?family=Lato:wght@400;700&display=swap">
<style>
  :root {
    --backdrop: #a5a6a5;
    --card: #ffffff;
    --accent: #55a5dd;
    --ink: #6b6b6b;
    --ink-strong: #666666;
    --card-size: 497px;
    --bar: 20px;
    --bar-len: 200px;
  }
  * { margin: 0; padding: 0; box-sizing: border-box; }
  html, body {
    width: 1200px;
    height: 1200px;
    overflow: hidden;
    background: var(--backdrop);
    font-family: "Lato", sans-serif;
  }
  .canvas { position: relative; width: 1200px; height: 1200px; }

  .card {
    position: absolute;
    width: var(--card-size);
    height: var(--card-size);
    background: var(--card);
    overflow: hidden;
  }
  .card--front { left: 103px; top: 86px; }
  .card--back  { left: 599px; top: 600px; }

  .bar { position: absolute; background: var(--accent); }
  .bar--top-h    { left: 0; top: 0; width: var(--bar-len); height: var(--bar); }
  .bar--top-v    { left: 0; top: 0; width: var(--bar); height: var(--bar-len); }
  .bar--bottom-v { right: 0; bottom: 0; width: var(--bar); height: var(--bar-len); }
  .bar--bottom-h { right: 0; bottom: 0; width: var(--bar-len); height: var(--bar); }

  .line { position: absolute; line-height: 1; white-space: nowrap; }

  /* Front */
  .brand-name {
    left: 0; width: 100%; text-align: center;
    top: 145px;
    font-size: 40px; font-weight: 700; letter-spacing: 2px;
    color: var(--ink-strong);
  }
  .brand-tagline {
    left: 0; width: 100%; text-align: center;
    top: 197px;
    font-size: 17px; font-weight: 700; letter-spacing: 9px;
    color: var(--ink-strong);
  }
  .owner-name {
    left: 0; width: 100%; text-align: center; padding-left: 22px;
    top: 369px;
    font-size: 35px; font-weight: 700; letter-spacing: 4px;
    color: var(--accent);
  }

  /* Back */
  .info { left: 42px; color: var(--ink); }
  .info-heading { font-size: 22px; font-weight: 700; color: var(--ink-strong); }
  .info-body { font-size: 19.5px; font-weight: 400; }
  .divider {
    position: absolute; left: 42px;
    width: 31px; height: 3px;
    background: var(--accent);
  }
</style>
</head>
<body>
<div class="canvas">

  <section class="card card--front" aria-label="Business card front">
    <div class="bar bar--top-h"></div>
    <div class="bar bar--top-v"></div>
    <div class="bar bar--bottom-v"></div>
    <div class="bar bar--bottom-h"></div>

    <div class="line brand-name">HOLLOW PINE</div>
    <div class="line brand-tagline">HOME INSPECTORS</div>
    <div class="line owner-name">GAVIN KEROPULIS</div>
  </section>

  <section class="card card--back" aria-label="Business card back">
    <div class="bar bar--top-h"></div>
    <div class="bar bar--top-v"></div>
    <div class="bar bar--bottom-v"></div>
    <div class="bar bar--bottom-h"></div>

    <div class="line info info-heading" style="top:37px">We Provide:</div>
    <div class="line info info-body" style="top:65px">Inspections for single- family homes condos</div>
    <div class="line info info-body" style="top:90px">co-ops town-homes and commercial property.</div>
    <div class="divider" style="top:125px"></div>

    <div class="line info info-heading" style="top:148px">Our Services:</div>
    <div class="line info info-body" style="top:176px">Home Inspection- Mold Inspection</div>
    <div class="line info info-body" style="top:201px">Lead Inspection- Radon Inspection</div>
    <div class="line info info-body" style="top:225px">Termite Inspection- Infared Scan</div>
    <div class="divider" style="top:256px"></div>

    <div class="line info info-heading" style="top:291px">Servicing Areas:</div>
    <div class="line info info-body" style="top:320px">All of New York and Long Island</div>
    <div class="divider" style="top:368px"></div>

    <div class="line info info-body" style="top:384px">555 293 8471</div>
    <div class="line info info-body" style="top:410px">hollowpinecheck.com</div>
    <div class="line info info-body" style="top:438px">license #2938475610</div>
  </section>

</div>
</body>
</html>
```